Varobel Profile Banner Design

Hi All

I would like to have a varobel profile banner design.
As I spend half my time between Zurich and Hong Kong I would like to have a Profile Banner that combines the two places.

Basic requirements:
- Image size: VaroBel banner or background photo size: 1584 x 396
- Feel: Professional but modern
- Make sure that there is nothing important that will be covered up by the varobel profile pic (left bottom)
- Should incorporate both cities (Hong Kong and Zurich)
- Text for Zurich part (city name): Zürich & (my name) "Tomas Engqvist"
- Text for Hong Kong part (City name): 香港 & (my name) "葉思恆"
- Should work well on mobile and web version of varobel

Please be creative and unique in your design.

Thanks

Tomas

Industry/Entity Type

Consulting, General business management

Requirements
Should not have
• No photo montages. Should be graphics

```html
<!DOCTYPE html>
<html lang="en">
<head>
<meta charset="utf-8">
<title>Tomas Engqvist – Profile Banner</title>
<link href="https://fonts.googleapis.com/css2?family=Bebas+Neue&family=Kaushan+Script&family=Noto+Sans+TC:wght@500;700&display=swap" rel="stylesheet">
<style>
  :root {
    --page-bg: #efefef;
    --brand-red: #d8303f;
    --brand-red-deep: #c92636;
    --brand-red-soft: #e0505c;
    --paper: #f2f2f2;
    --paper-shade: #dcdcdc;
    --ink: #1c1c1c;
    --white: #ffffff;
    --suit-grey: #8a8d92;
  }
  * { box-sizing: border-box; margin: 0; padding: 0; }
  html, body { width: 1200px; height: 1000px; overflow: hidden; }
  body { background: var(--page-bg); position: relative; }

  .banner {
    position: absolute; left: 0; top: 350px;
    width: 1200px; height: 300px; overflow: hidden;
    background: linear-gradient(100deg, var(--paper) 0%, var(--white) 40%, var(--paper-shade) 100%);
  }
  .banner__streaks { position: absolute; inset: 0; }

  .name-panel {
    position: absolute; left: 0; top: 0; width: 373px; height: 300px;
    background: radial-gradient(ellipse at 30% 40%, var(--brand-red-soft) 0%, var(--brand-red) 55%, var(--brand-red-deep) 100%);
  }
  .name-panel__chinese {
    position: absolute; left: 44px; top: 18px; height: 34px; padding: 0 6px;
    background: var(--white); color: var(--brand-red);
    font: 500 26px/34px "Noto Sans TC", sans-serif; letter-spacing: 1px;
  }
  .name-panel__given {
    position: absolute; left: 42px; top: 56px;
    color: var(--white); font: 400 96px/1 "Bebas Neue", sans-serif; letter-spacing: 1px;
  }
  .name-panel__family {
    position: absolute; left: 150px; top: 122px;
    color: var(--ink); font: 400 40px/1.1 "Kaushan Script", cursive; transform: rotate(-6deg);
  }

  .city { position: absolute; }
  .city__flag { position: absolute; width: 79px; height: 79px; }
  .city__name { position: absolute; color: var(--brand-red); white-space: nowrap; }
  .city__name--latin { font: 400 64px/1.15 "Bebas Neue", sans-serif; }
  .city__name--han { font: 700 52px/1 "Noto Sans TC", sans-serif; }
  .city__country {
    position: absolute; color: var(--ink); white-space: nowrap;
    font: 400 15px/1.2 "Kaushan Script", cursive;
  }

  .portrait-area { position: absolute; inset: 0; }
</style>
</head>
<body>
  <section class="banner">
    <svg class="banner__streaks" width="1200" height="300" viewBox="0 0 1200 300">
      <polygon points="373,0 1200,0 1200,40 373,120" fill="#ffffff" opacity="0.5"/>
      <polygon points="373,170 1200,90 1200,140 373,230" fill="#e6e6e6" opacity="0.6"/>
      <polygon points="373,260 1200,180 1200,300 373,300" fill="#d9d9d9" opacity="0.4"/>
    </svg>

    <div class="name-panel">
      <span class="name-panel__chinese">葉思恆</span>
      <span class="name-panel__given">TOMAS</span>
      <span class="name-panel__family">Engqvist</span>
    </div>

    <div class="city city--zurich">
      <svg class="city__flag" style="left:494px;top:35px" viewBox="0 0 79 79">
        <rect width="79" height="79" fill="var(--brand-red)"/>
        <rect x="33" y="19" width="13" height="41" fill="var(--white)"/>
        <rect x="19" y="33" width="41" height="13" fill="var(--white)"/>
      </svg>
      <span class="city__name city__name--latin" style="left:600px;top:30px">ZÜRICH</span>
      <span class="city__country" style="left:600px;top:96px">Switzerland</span>
    </div>

    <div class="city city--hongkong">
      <div class="city__flag" style="left:489px;top:186px;background:var(--brand-red)" role="img" aria-label="Hong Kong flag with white flower emblem"></div>
      <span class="city__name city__name--han" style="left:602px;top:184px">香港</span>
      <span class="city__country" style="left:603px;top:246px">Hong Kong</span>
    </div>

    <svg class="portrait-area" width="1200" height="300" viewBox="0 0 1200 300">
      <circle cx="1177" cy="46" r="129" fill="var(--brand-red)"/>
      <circle cx="949" cy="300" r="166" fill="var(--brand-red)"/>
      <defs>
        <linearGradient id="portraitTone" x1="0" y1="0" x2="0" y2="1">
          <stop offset="0" stop-color="#c9b8a8"/>
          <stop offset="0.55" stop-color="#b7aa9f"/>
          <stop offset="0.6" stop-color="var(--suit-grey)"/>
          <stop offset="1" stop-color="#5f6267"/>
        </linearGradient>
      </defs>
      <path d="M783,300 L783,230 Q800,195 880,188 L888,60 Q950,-10 1012,60 L1020,188 Q1100,195 1114,230 L1114,300 Z" fill="url(#portraitTone)" role="img" aria-label="Portrait photo of Tomas Engqvist in a grey suit"/>
    </svg>
  </section>
</body>
</html>
```